Lantern over the Harbor ~ A Widening Passage for Writers

My book is called “Lantern over the Harbor.” Its subtitle is “A Widening Passage for Writers.” It is a book about being a poet, writing poetry, and the ways in which poets are connected to both society and the central energy of the Universe. I want the cover design to be abstract and impressionistic. A suggestion of fireworks or a starburst would be a plus. To be consistent with the 3 other books I have published, I want the font for the title, as well as my name (Dorothea Quillbrake) to be Papyrus. The subtitle font can be something more plain and sans serif, like Arial or Franklin Gothic Book, probably in italics. As for color, I definitely want pale gold (angelic). Possible other complimentary colors could be either light or dark shades of gray, turquoise, rose, rust or red. I'm attaching the back cover text and also three pages from inside the book that have line drawings, to give an example of the interior artwork.
Updates

Forgot to mention: My book is a paperback. Its size will be 8.5" high and 5.5" wide. I'm self-publishing it, and it will be printed by Halvern Printworks in Nebraska, USA. It has 104 pages. I think you need the number of pages, in order to make the spine of the book the correct width.

Target Market(s)

My target market is people who write poetry or are interested in how poetry is written.

Industry/Entity Type

Poetry

Font styles to use
Sans Serif
Other font styles liked:
• Papyrus for the front cover. Arial or another sans serif font on the back cover.

Colors

Designer to choose colors to be used in the design.

Requirements
Must have
• My book cover needs to be inspiring and uplifting, as well as abstract and impressionistic, with kind of a "New Age" feel. I don't want anything that looks rigid and scholarly.
Nice to have
• The book talks about the connection poets have to the Universe and the Creative Energy at the center of everything. The cover should convey that Energy.
Should not have
• My cover should not be realistic, logical or straight-laced. I want something that feels free, imaginative and unfettered.

```html
<!DOCTYPE html>
<html lang="en">
<head>
<meta charset="utf-8">
<title>Lantern over the Harbor – Cover Spread</title>
<link rel="stylesheet" href="https://fonts.googleapis.com/css2?family=Macondo&family=Arimo:ital,wght@0,700;1,700&family=Open+Sans:ital,wght@0,400;0,700;1,400;1,700&display=swap">
<style>
  :root {
    --paper: #ffffff;
    --cover-black: #000000;
    --text-light: #ffffff;
    --crop-grey: #b5b5b5;
    --label-ink: #111111;
    --burst-core: #ffd36a;
    --burst-mid: #f08a24;
    --burst-rim: #b8301a;
    --ornament-grey: #9a9a9a;
    --portrait-tone: #b9a79c;
  }
  * { box-sizing: border-box; margin: 0; padding: 0; }
  html, body { width: 1200px; height: 942px; overflow: hidden; background: var(--paper); }
  .sheet { position: relative; width: 1200px; height: 942px; background: var(--paper); }

  .crop-marks { position: absolute; inset: 0; }

  .cover {
    position: absolute; left: 72px; top: 72px; width: 1086px; height: 798px;
    background: var(--cover-black); color: var(--text-light);
  }

  /* Back cover */
  .back {
    position: absolute; left: 35px; top: 22px; width: 455px;
    font-family: "Open Sans", Arial, sans-serif; font-size: 13.6px; line-height: 19.4px;
    text-align: justify;
  }
  .back p { margin-bottom: 10px; }
  .back .chapters-intro { text-align: center; margin-bottom: 8px; }
  .back .chapters { text-align: center; line-height: 21px; margin-bottom: 14px; }
  .ornament-slot { display: block; width: 82px; height: 40px; margin: 0 auto 22px; }
  .author-portrait {
    float: left; width: 98px; height: 101px; margin: 4px 10px 2px 0;
    background: linear-gradient(160deg, #d8d2cc, var(--portrait-tone) 55%, #8f7b70);
  }
  .bio { hyphens: auto; }
  .back em { font-style: italic; }
  .barcode-box { position: absolute; left: 328px; top: 644px; width: 153px; height: 116px; background: var(--paper); }

  /* Spine */
  .spine-text {
    position: absolute; left: 526px; width: 24px;
    writing-mode: vertical-rl; font-family: "Open Sans", Arial, sans-serif;
    font-size: 12.5px; letter-spacing: 2.2px; color: var(--text-light); white-space: nowrap;
  }
  .spine-title { top: 14px; }
  .spine-author { top: 545px; }

  /* Front cover */
  .burst {
    position: absolute; left: 540px; top: 150px; width: 460px; height: 610px;
    background: radial-gradient(ellipse 50% 45% at 52% 48%, var(--burst-core) 0%, var(--burst-mid) 30%, var(--burst-rim) 60%, rgba(184,48,26,0) 100%);
    opacity: .9;
  }
  .front-title {
    position: absolute; left: 560px; top: 8px; width: 500px; text-align: center;
    font-family: "Macondo", "Papyrus", fantasy; font-weight: 400; color: var(--text-light);
    font-size: 84px; line-height: 76px;
  }
  .front-title span { display: block; }
  .front-subtitle {
    position: absolute; left: 560px; top: 275px; width: 500px; text-align: center;
    font-family: "Arimo", Arial, sans-serif; font-weight: 700; font-size: 22px; color: var(--text-light);
    text-shadow: 1px 2px 3px rgba(0,0,0,.9);
  }
  .front-author {
    position: absolute; left: 560px; top: 718px; width: 500px; text-align: center;
    font-family: "Macondo", "Papyrus", fantasy; font-size: 42px; color: var(--text-light);
  }

  .trim-size {
    position: absolute; left: 292px; top: 890px;
    font-family: "Arimo", Arial, sans-serif; font-weight: 700; font-size: 21px; color: var(--label-ink);
  }
</style>
</head>
<body>
<div class="sheet">
  <svg class="crop-marks" width="1200" height="942" aria-hidden="true">
    <g stroke="var(--crop-grey)" stroke-width="1" stroke-dasharray="6 4">
      <line x1="72" y1="0" x2="72" y2="52"/><line x1="72" y1="890" x2="72" y2="942"/>
      <line x1="596" y1="0" x2="596" y2="52"/><line x1="596" y1="890" x2="596" y2="942"/>
      <line x1="613" y1="0" x2="613" y2="52"/><line x1="613" y1="890" x2="613" y2="942"/>
      <line x1="1158" y1="0" x2="1158" y2="52"/><line x1="1158" y1="890" x2="1158" y2="942"/>
      <line x1="0" y1="72" x2="52" y2="72"/><line x1="1178" y1="72" x2="1200" y2="72"/>
      <line x1="0" y1="870" x2="52" y2="870"/><line x1="1178" y1="870" x2="1200" y2="870"/>
    </g>
  </svg>

  <div class="cover">
    <section class="back">
      <p><strong><em>Lantern over the Harbor</em></strong> is indeed “A Widening Passage for Writers.” It is written by Dorothea Quillbrake, an exciting, imaginative voice in American poetry.</p>
      <p>In <em>Lantern over the Harbor</em>, Dorothea discusses the essential elements of poetry and the process of writing it. She offers an inspiring view of the mission of poets and their connection to both society and the larger forces in the Universe. Her book is motivational, refreshing and irrepressibly optimistic.</p>
      <p class="chapters-intro">The seven intriguing chapters in <strong><em>Lantern over the Harbor</em></strong> are</p>
      <p class="chapters">LIBERATION ~ EXPERIENCE ~ WORDS ~ POETRY ~<br>INTEGRITY ~ BEAUTY ~ CREATION</p>
      <svg class="ornament-slot" viewBox="0 0 82 40" role="img" aria-label="Small grey shell-like ornament">
        <defs><linearGradient id="orn" x1="0" x2="1"><stop offset="0" stop-color="#6f6f6f"/><stop offset="1" stop-color="#d0d0d0"/></linearGradient></defs>
        <rect x="0" y="4" width="82" height="32" rx="16" fill="url(#orn)"/>
      </svg>
      <div class="author-portrait" role="img" aria-label="Portrait photograph of the author"></div>
      <p class="bio">For over 50 years, Dorothea has been a teacher of writing and poetry. Since 2007, she has published three books of her poems: <em>Under the Copper Kettle, The Pale Hem of Morning</em> and <em>The Quiet Linen Sky</em>. Her work overflows with her characteristically rich images and quirky metaphors. It runs the gamut from subtle eroticism to abject grief, from defiant rage to philosophical meditation, and from borderline blasphemy to lyrical fantasy.</p>
      <p>Dorothea has been called by critic Gerald Ashcombe “a poet to be reckoned with; bright, feisty, compassionate.” (<em>The Valley Courier</em>, Millbrook, OH). Author Loretta Vance (“<em>Ashgrove</em>,” 2011) says Dorothea’s poetry is like “a perpetual Surprise Party ~ memorable, insightful and thematically fascinating.”</p>
    </section>
    <div class="barcode-box"></div>

    <div class="spine-text spine-title">LANTERN OVER THE HARBOR</div>
    <div class="spine-text spine-author">DOROTHEA QUILLBRAKE</div>

    <div class="burst" role="img" aria-label="Abstract burst of scattered gold, orange and red fireworks fragments"></div>
    <h1 class="front-title"><span>Lantern</span><span>over the</span><span>Harbor</span></h1>
    <p class="front-subtitle">A Widening Passage for Writers</p>
    <p class="front-author">Dorothea Quillbrake</p>
  </div>

  <div class="trim-size">5.5 x 8.5</div>
</div>
</body>
</html>
```